Combined entities letterhead

Hi
We need to combine our two sister business's logos onto a letterhead for invoicing and they will need to come under the banner of Coolvane Systems Pty Ltd.
I have attached our current logos, a copy of our current letterheads for Cool Vane WA and Coolvane Systems Pty Ltd. The idea would be to have the Coolvane Systems logo on top (with the words incorporating) and the 2 sister businesses under it in the header, or something similar. Some of the wording may need to be changed as far as contact numbers and addresses but I just want to get the basics layout completed first.

```html
<!DOCTYPE html>
<html lang="en">
<head>
<meta charset="utf-8">
<title>Cool Vane WA – Letterhead</title>
<link rel="stylesheet" href="https://fonts.googleapis.com/css2?family=Roboto+Condensed:wght@700&family=Montserrat:wght@400;600;700&family=Questrial&family=Open+Sans:wght@600&family=Lato:wght@400;700&display=swap">
<style>
  :root {
    --brand-blue: #2553a5;
    --brand-green: #4bb848;
    --brand-navy: #14305a;
    --text-grey: #9a9a9a;
    --body-grey: #a3a3a3;
    --contact-grey: #5a5a5a;
    --backdrop: #ebecee;
    --paper: #ffffff;
  }
  html, body {
    margin: 0;
    width: 1068px;
    height: 1200px;
    overflow: hidden;
    background: var(--backdrop);
  }
  .sheet-holder {
    position: absolute;
    left: 106px;
    top: 0;
    width: 855px;
    height: 1200px;
  }
  .sheet {
    position: absolute;
    left: 0;
    top: 0;
    width: 1201px;
    height: 1685px;
    background: var(--paper);
    transform: scale(0.7122);
    transform-origin: 0 0;
    overflow: hidden;
  }
  .abs { position: absolute; margin: 0; }

  /* Header */
  .brand-name {
    left: 60px; top: 102px;
    font: 700 72px/1 "Roboto Condensed", sans-serif;
    color: var(--brand-blue);
    letter-spacing: 1px;
    white-space: nowrap;
  }
  .sister-title {
    left: 57px; top: 210px;
    font: 700 35px/1 "Roboto Condensed", sans-serif;
    color: var(--brand-blue);
    white-space: nowrap;
  }
  .header-rule { left: 410px; top: 231px; }
  .sister-name {
    right: 82px; top: 136px;
    font: 700 30px/1.15 "Montserrat", sans-serif;
    color: var(--brand-navy);
    text-align: right;
    letter-spacing: 1px;
  }

  /* Recipient */
  .recipient { left: 122px; top: 380px; color: var(--text-grey); }
  .recipient-name {
    font: 600 30px/1.1 "Montserrat", sans-serif;
    margin: 0 0 14px;
  }
  .recipient-line {
    font: 400 19px/1.5 "Montserrat", sans-serif;
    margin: 0 0 7px;
  }
  .recipient-line.address { line-height: 28px; }
  .letter-date {
    right: 123px; top: 550px;
    font: 600 24px/1 "Open Sans", sans-serif;
    color: var(--text-grey);
  }

  /* Body */
  .letter-body {
    left: 122px; top: 612px; width: 956px;
    font: 400 22px/37px "Questrial", sans-serif;
    color: var(--body-grey);
  }
  .letter-body p { margin: 0 0 37px; }
  .letter-body .line {
    display: block;
    white-space: nowrap;
    text-align: justify;
    text-align-last: justify;
  }
  .letter-body .line.last { text-align: left; text-align-last: left; }

  /* Sign-off */
  .signer-name {
    left: 815px; top: 1194px;
    font: 600 37px/1 "Montserrat", sans-serif;
    color: var(--text-grey);
  }
  .signature-area {
    left: 850px; top: 1255px; width: 175px; height: 110px;
    background: #f2f2f2;
  }

  /* Footer */
  .footer-links {
    left: 53px; top: 1486px; width: 1100px;
    font: 700 19px/1 "Lato", sans-serif;
    color: var(--brand-blue);
  }
  .footer-links span { position: absolute; top: 0; white-space: nowrap; }
  .office-band { left: 0; top: 1525px; }
  .band-label {
    top: 1533px;
    font: 700 21px/1 "Lato", sans-serif;
    color: #fff;
  }
  .contact-col {
    top: 1585px;
    font: 400 19px/1 "Lato", sans-serif;
    color: var(--contact-grey);
  }
  .contact-row { display: flex; align-items: center; gap: 7px; height: 22px; margin-bottom: 12px; white-space: nowrap; }
  .contact-row svg { width: 22px; height: 22px; flex: none; }
</style>
</head>
<body>
<div class="sheet-holder">
  <div class="sheet">

    <header>
      <h1 class="abs brand-name">COOL VANE WA</h1>
      <h2 class="abs sister-title">2 SISTER BUSINESSES</h2>
      <svg class="abs header-rule" width="791" height="6" viewBox="0 0 791 6">
        <rect x="0" y="0" width="116" height="4" fill="var(--brand-green)"/>
        <rect x="123" y="0" width="12" height="4" fill="var(--brand-green)"/>
        <rect x="141" y="0" width="12" height="4" fill="var(--brand-green)"/>
        <rect x="159" y="0" width="12" height="4" fill="var(--brand-green)"/>
        <rect x="177" y="0" width="12" height="4" fill="var(--brand-green)"/>
        <rect x="196" y="0" width="595" height="4" fill="var(--brand-blue)"/>
      </svg>
      <p class="abs sister-name">KESTREL<br>AIRCONDITIONING</p>
    </header>

    <section class="abs recipient">
      <p class="recipient-name">ALEX MORGAN</p>
      <p class="recipient-line">0123-456-789</p>
      <p class="recipient-line">info@youremailaddress.com</p>
      <p class="recipient-line address">1234 City Your Ln. Suite<br>123 Dallas, TX 0000</p>
    </section>
    <p class="abs letter-date">12 December, 2023</p>

    <main class="abs letter-body">
      <p>
        <span class="line">Lorem ipsum dolor sit amet, consectetuer adipiscing elit, sed diam nonummy nibh euismod</span>
        <span class="line">tincidunt ut laoreet dolore magna aliquam erat volutpat. Ut wisi enim ad minim veniam, quis</span>
        <span class="line">nostrud exerci tation ullamcorper suscipit lobortis nisl ut aliquip ex ea commodo consequat.</span>
        <span class="line">Duis autem vel eum iriure dolor in hendrerit in vulputate velit esse molestie consequat, vel</span>
        <span class="line">illum dolore eu feugiat nulla facilisis at vero eros et accumsan et iusto odio dignissim qui</span>
        <span class="line last">blandit praesent luptatum zzril delenit augue duis dolore te feugait nulla facilisi.</span>
      </p>
      <p>
        <span class="line">Lorem ipsum dolor sit amet, cons ectetuer adipiscing elit, sed diam nonummy nibh euismod</span>
        <span class="line">tincidunt ut laoreet dolore magna aliquam erat volutpat. Ut wisi enim ad minim veniam, quis</span>
        <span class="line last">nostrud exerci tation ullamcorper suscipit lobortis nisl ut aliquip ex ea commodo consequat.</span>
      </p>
      <p>
        <span class="line">Lorem ipsum dolor sit amet, consectetuer adipiscing elit, sed diam nonummy nibh euismod</span>
        <span class="line last">tincidunt ut laoreet dolore magna aliquam erat</span>
      </p>
    </main>

    <p class="abs signer-name">ALEX MORGAN</p>
    <div class="abs signature-area" role="img" aria-label="Handwritten signature of the sender"></div>

    <footer>
      <div class="abs footer-links">
        <span style="left:0">info@coolvane.com.au</span>
        <span style="left:320px">www.coolvane.com.au</span>
        <span style="left:693px">ABN 12 345 678 901</span>
        <span style="left:907px">AU41529</span>
        <span style="left:1015px">EC27384</span>
      </div>

      <svg class="abs office-band" width="1201" height="39" viewBox="0 0 1201 39">
        <polygon points="0,0 224,0 212,39 0,39" fill="var(--brand-blue)"/>
        <polygon points="240,0 263,0 251,39 228,39" fill="var(--brand-green)"/>
        <polygon points="278,0 301,0 289,39 266,39" fill="var(--brand-green)"/>
        <polygon points="316,0 339,0 327,39 304,39" fill="var(--brand-green)"/>
        <polygon points="359,0 1201,0 1201,39 347,39" fill="var(--brand-green)"/>
      </svg>
      <span class="abs band-label" style="left:53px">Head Office</span>
      <span class="abs band-label" style="left:680px">Branch</span>

      <div class="abs contact-col" style="left:55px">
        <div class="contact-row">
          <svg viewBox="0 0 22 22"><rect width="22" height="22" rx="4" fill="var(--brand-green)"/><path d="M7 5c1 0 2 2.5 2 3.3 0 .8-1 1.1-1 1.7.4 1.6 2.1 3.3 3.7 3.8.6 0 .9-1 1.7-1 .8 0 3.4 1 3.4 2S15.5 17 14.5 17C9.6 17 5 12.4 5 7.5 5 6.5 6 5 7 5z" fill="#fff"/></svg>
          <span>01234 56 78 90</span>
        </div>
        <div class="contact-row">
          <svg viewBox="0 0 22 22"><rect width="22" height="22" rx="4" fill="var(--brand-green)"/><rect x="4.5" y="6.5" width="13" height="9" fill="none" stroke="#fff" stroke-width="1.5"/><path d="M4.5 6.5l6.5 5 6.5-5M4.5 15.5l4.5-4.5M17.5 15.5L13 11" fill="none" stroke="#fff" stroke-width="1.3"/></svg>
          <span>info@mailaddress.com</span>
        </div>
      </div>

      <div class="abs contact-col" style="left:367px">
        <div class="contact-row">
          <svg viewBox="0 0 22 22"><rect width="22" height="22" rx="4" fill="var(--brand-blue)"/><path d="M7 5c1 0 2 2.5 2 3.3 0 .8-1 1.1-1 1.7.4 1.6 2.1 3.3 3.7 3.8.6 0 .9-1 1.7-1 .8 0 3.4 1 3.4 2S15.5 17 14.5 17C9.6 17 5 12.4 5 7.5 5 6.5 6 5 7 5z" fill="#fff"/></svg>
          <span>01234 56 78 90</span>
        </div>
        <div class="contact-row">
          <svg viewBox="0 0 22 22"><rect width="22" height="22" rx="4" fill="var(--brand-blue)"/><rect x="4.5" y="6.5" width="13" height="9" fill="none" stroke="#fff" stroke-width="1.5"/><path d="M4.5 6.5l6.5 5 6.5-5M4.5 15.5l4.5-4.5M17.5 15.5L13 11" fill="none" stroke="#fff" stroke-width="1.3"/></svg>
          <span>info@mailaddress.com</span>
        </div>
      </div>

      <div class="abs contact-col" style="left:648px">
        <div class="contact-row">
          <svg viewBox="0 0 22 22"><rect width="22" height="22" rx="4" fill="var(--brand-blue)"/><path d="M7 5c1 0 2 2.5 2 3.3 0 .8-1 1.1-1 1.7.4 1.6 2.1 3.3 3.7 3.8.6 0 .9-1 1.7-1 .8 0 3.4 1 3.4 2S15.5 17 14.5 17C9.6 17 5 12.4 5 7.5 5 6.5 6 5 7 5z" fill="#fff"/></svg>
          <span>01234 56 78 90</span>
        </div>
        <div class="contact-row">
          <svg viewBox="0 0 22 22"><rect width="22" height="22" rx="4" fill="var(--brand-blue)"/><rect x="4.5" y="6.5" width="13" height="9" fill="none" stroke="#fff" stroke-width="1.5"/><path d="M4.5 6.5l6.5 5 6.5-5M4.5 15.5l4.5-4.5M17.5 15.5L13 11" fill="none" stroke="#fff" stroke-width="1.3"/></svg>
          <span>info@mailaddress.com</span>
        </div>
      </div>

      <div class="abs contact-col" style="left:928px">
        <div class="contact-row">
          <svg viewBox="0 0 22 22"><rect width="22" height="22" rx="4" fill="var(--brand-blue)"/><path d="M7 5c1 0 2 2.5 2 3.3 0 .8-1 1.1-1 1.7.4 1.6 2.1 3.3 3.7 3.8.6 0 .9-1 1.7-1 .8 0 3.4 1 3.4 2S15.5 17 14.5 17C9.6 17 5 12.4 5 7.5 5 6.5 6 5 7 5z" fill="#fff"/></svg>
          <span>01234 56 78 90</span>
        </div>
        <div class="contact-row">
          <svg viewBox="0 0 22 22"><rect width="22" height="22" rx="4" fill="var(--brand-blue)"/><rect x="4.5" y="6.5" width="13" height="9" fill="none" stroke="#fff" stroke-width="1.5"/><path d="M4.5 6.5l6.5 5 6.5-5M4.5 15.5l4.5-4.5M17.5 15.5L13 11" fill="none" stroke="#fff" stroke-width="1.3"/></svg>
          <span>info@mailaddress.com</span>
        </div>
      </div>
    </footer>

  </div>
</div>
</body>
</html>
```